Business Card Design Project

I need a template business card for a web design / software company called

"Design marrowind"

we specialize in propelling archaic paper-based processes into the fore of the 21st century with web based solutions, graphical interfaces, graphic design outsourcing, automation software deployments, database design and development, segmentation of data and preservation of data integrity.

http://lexicon.wordquarry.com/browse/phenomena
British Dictionary definitions for phenomena

phenomena
/fɪˈnɒmɪnə/
noun
1.
a plural of phenomenon
phenomenon
/fɪˈnɒmɪnən/
noun (pl) -ena (-ɪnə), -enons
1.
anything that can be perceived as an occurrence or fact by the senses
2.
any remarkable occurrence or person
3.
(philosophy)

the object of perception, experience, etc
(in the writings of Brell) a thing as it appears and is interpreted in perception and reflection, as distinguished from its real nature as a thing-in-itself Compare noumenon
"

I am very open minded here I am letting you take the design and run with it...

good luck

Target Market(s)

Professional companies, small business in western speaking countries in need of collating design capabilities for web pages, web stores, graphic design or software development projects

Industry/Entity Type

Graphic Design

Colors

Designer to choose colors to be used in the design.

Requirements
Must have
• Designed in Adobe Illustrator

```html
<!DOCTYPE html>
<html lang="en">
<head>
<meta charset="utf-8">
<title>Design Marrowind – Business Card</title>
<link rel="stylesheet" href="https://fonts.googleapis.com/css2?family=Barlow+Semi+Condensed:wght@400&display=swap">
<style>
  :root {
    --card-bg: #ffffff;
    --pattern-tone: #e4f2f8;
    --pattern-tone-deep: #d6ebf4;
    --ink: #587580;
  }
  html, body {
    margin: 0;
    padding: 0;
    overflow: hidden;
    background: var(--card-bg);
  }
  .card {
    position: relative;
    width: 1200px;
    height: 720px;
    overflow: hidden;
    background: var(--card-bg);
    font-family: "Barlow Semi Condensed", "Arial Narrow", sans-serif;
    color: var(--ink);
  }
  .card__pattern {
    position: absolute;
    inset: 0;
    background: linear-gradient(180deg, var(--pattern-tone) 0%, var(--pattern-tone-deep) 50%, var(--pattern-tone) 100%);
  }
  .card__brand {
    position: absolute;
    left: 62px;
    top: 448px;
    margin: 0;
    font-size: 158px;
    font-weight: 400;
    line-height: 1;
    letter-spacing: -1px;
    white-space: nowrap;
  }
  .card__contact {
    position: absolute;
    left: 0;
    top: 0;
    width: 380px;
    margin: 0;
    padding: 0;
    list-style: none;
    transform-origin: 0 0;
    transform: translate(876px, 453px) rotate(-90deg);
    font-size: 38px;
    line-height: 53px;
    white-space: nowrap;
  }
  .card__contact li {
    text-align: left;
  }
</style>
</head>
<body>
  <main class="card">
    <div class="card__pattern" role="img" aria-label="Light blue pattern of interlocking rings covering the card"></div>
    <h1 class="card__brand">Design Marrowind</h1>
    <ul class="card__contact">
      <li class="card__name">John Smith</li>
      <li class="card__role">Job Title</li>
      <li class="card__tel">Tel. +1234567890</li>
      <li class="card__cell">cell +1234567890</li>
      <li class="card__email">@: jsmith@d.marrow.com</li>
    </ul>
  </main>
</body>
</html>
```